Barrister Letterhead incorporating existing logo/design

Require new letterhead template to incorporate logo and information on 'Letter 2015' word document. Currently the information on the letterhead is very busy and would like a cleaner look.
Must look good in black and white, and colour when printed.

Target Market(s)

Professional

Industry/Entity Type

Legal

Requirements
Must have
• Clean professional look.

```html
<!DOCTYPE html>
<html lang="en">
<head>
<meta charset="utf-8">
<title>Halloran Chambers Letterhead</title>
<link href="https://fonts.googleapis.com/css2?family=Tinos&display=swap" rel="stylesheet">
<style>
  :root {
    --backdrop: #d2d2d2;
    --paper: #fafafa;
    --navy: #1a2a4a;
    --swoosh: #9a9a9a;
    --ink: #3a3a3a;
    --on-navy: #ffffff;
    --on-navy-soft: #d9dee8;
  }
  html, body {
    margin: 0;
    padding: 0;
    width: 1200px;
    height: 1172px;
    overflow: hidden;
    background: var(--backdrop);
  }
  .letterhead {
    position: absolute;
    left: 210px;
    top: 30px;
    width: 780px;
    height: 1112px;
    display: block;
  }
  .paper { fill: var(--paper); }
  .header-band { fill: var(--navy); }
  .swoosh { fill: var(--swoosh); }
  .brand-mark { fill: none; stroke: var(--on-navy); stroke-width: 1.6; }
  .brand-name {
    font-family: "Tinos", "Times New Roman", serif;
    font-size: 24px;
    fill: var(--on-navy);
    letter-spacing: 0.3px;
  }
  .abn {
    font-family: "Tinos", "Times New Roman", serif;
    font-size: 7.6px;
    fill: var(--on-navy-soft);
  }
  .contact-text {
    font-family: "Tinos", "Times New Roman", serif;
    font-size: 7.6px;
    fill: var(--ink);
  }
  .contact-icon { fill: var(--ink); }
  .contact-icon-line { fill: none; stroke: var(--ink); stroke-width: 0.8; }
</style>
</head>
<body>
<svg class="letterhead" viewBox="0 0 656 935" xmlns="http://www.w3.org/2000/svg" aria-label="Halloran Chambers letterhead">
  <rect class="paper" x="0" y="0" width="656" height="935"/>

  <!-- header band and swooshes -->
  <path class="header-band" d="M0,0 H656 V160 C565,160 485,118 405,74 C320,28 220,4 120,4 C60,4 22,10 0,16 Z"/>
  <path class="swoosh" d="M0,24 C100,8 250,12 360,62 C460,112 545,158 656,160 L656,168 C540,166 450,122 350,78 C250,34 120,20 0,32 Z"/>
  <path class="swoosh" d="M0,50 C110,32 250,34 340,64 C250,46 120,46 0,58 Z"/>

  <!-- brand -->
  <g class="brand">
    <rect class="brand-mark" x="425" y="36" width="48" height="48"/>
    <text class="brand-name" x="620" y="58" text-anchor="end">HALLORAN</text>
    <text class="brand-name" x="620" y="81" text-anchor="end">CHAMBERS</text>
    <text class="abn" x="620" y="108" text-anchor="end">ABN 11 222 333 444</text>
  </g>

  <!-- contact details -->
  <g class="contact">
    <!-- phone -->
    <path class="contact-icon" d="M36,98 h7 v1.5 h-1.6 l-0.6,-0.8 h-2.6 l-0.6,0.8 h-1.6 z M37,100.5 h5 l0.6,2.5 h-6.2 z"/>
    <text class="contact-text" x="50" y="103">07 4000 1234</text>
    <!-- fax -->
    <path class="contact-icon" d="M97,97.5 h4 v2 h-4 z M95.5,100 h7 v2.6 h-7 z M97,102.6 h4 v1.4 h-4 z"/>
    <text class="contact-text" x="105" y="103">07 4000 5678</text>
    <!-- mail -->
    <rect class="contact-icon" x="35.5" y="110" width="7" height="4.6"/>
    <path d="M35.5,110 L39,112.6 L42.5,110" fill="none" stroke="#fafafa" stroke-width="0.7"/>
    <text class="contact-text" x="50" y="115">clerk@qldcounsel.au</text>
    <!-- globe -->
    <circle class="contact-icon-line" cx="39" cy="124" r="3"/>
    <ellipse class="contact-icon-line" cx="39" cy="124" rx="1.3" ry="3"/>
    <line class="contact-icon-line" x1="36" y1="124" x2="42" y2="124"/>
    <text class="contact-text" x="50" y="127">www.hallorannchambers.com.au</text>
    <!-- pin -->
    <path class="contact-icon" d="M39,131.5 a2.6,2.6 0 0 1 2.6,2.6 c0,2 -2.6,4.6 -2.6,4.6 c0,0 -2.6,-2.6 -2.6,-4.6 a2.6,2.6 0 0 1 2.6,-2.6 z"/>
    <circle cx="39" cy="134.1" r="0.9" fill="#fafafa"/>
    <text class="contact-text" x="50" y="139">Level 1 42 Flinders Lane, Riverton</text>
    <text class="contact-text" x="50" y="150">P.O. Box 218, Riverton. Q. 4900</text>
  </g>
</svg>
</body>
</html>
```